Vardel paint banner

Banner same size Lumora Solutions advert banner
of previous one Lumora Solutions advert banner 215cm x 1055cm
but for a paint company, called Vardel Paint.
I want the concept to be similar to the attached, i want to put some real drum paint in front of the banner concept to look in Harmony with your concept on the banner.
The company is specialized in producing and painting houses and offices indoor and outdoor and applying epoxy on floors..

```html
<!DOCTYPE html>
<html lang="en">
<head>
<meta charset="utf-8">
<title>Vardel Paint Banner</title>
<link rel="stylesheet" href="https://fonts.googleapis.com/css2?family=Exo+2:wght@500;700&family=Fraunces:opsz,wght@9..144,700&display=swap">
<style>
  :root {
    --stage: #a7a7a7;
    --navy-deep: #0b2f57;
    --navy: #13477c;
    --sky: #6fa6d8;
    --sky-light: #b9d6ef;
    --mist: #d4e4f3;
    --brand-blue: #3b82c8;
    --headline-ink: #4a4a57;
    --invite-ink: #e6e1ef;
    --invite-shadow: rgba(40, 50, 80, 0.55);
    --white: #ffffff;
    --can-blue: #2f8fe0;
    --can-silver: #c9d3dd;
  }
  * { margin: 0; padding: 0; box-sizing: border-box; }
  html, body {
    width: 1200px;
    height: 251px;
    overflow: hidden;
    background: var(--stage);
  }
  .banner {
    position: absolute;
    left: 9px;
    top: 7px;
    width: 1100px;
    height: 223px;
    overflow: hidden;
    background:
      radial-gradient(ellipse at 62% 45%, var(--mist) 0%, rgba(212,228,243,0) 45%),
      linear-gradient(90deg, var(--navy-deep) 0%, var(--navy) 28%, var(--sky) 44%, var(--sky-light) 60%, var(--mist) 80%, var(--sky-light) 100%);
    box-shadow: 12px 12px 14px rgba(0, 0, 0, 0.35);
    font-family: "Exo 2", sans-serif;
  }
  .brand {
    position: absolute;
    left: 16px;
    top: 36px;
    display: flex;
    align-items: center;
    gap: 18px;
  }
  .brand-dot {
    width: 118px;
    height: 118px;
    border-radius: 50%;
    background: var(--brand-blue);
  }
  .brand-name {
    font-family: "Exo 2", sans-serif;
    font-weight: 700;
    font-size: 62px;
    line-height: 60px;
    color: var(--brand-blue);
    text-transform: uppercase;
    letter-spacing: -1px;
  }
  .headline {
    position: absolute;
    left: 447px;
    top: 20px;
    font-weight: 500;
    font-size: 28px;
    color: var(--headline-ink);
    text-shadow: 1px 1px 2px rgba(255, 255, 255, 0.6);
    white-space: nowrap;
  }
  .invite {
    position: absolute;
    left: 468px;
    top: 60px;
    width: 420px;
    text-align: center;
    font-weight: 500;
    font-size: 28px;
    line-height: 35px;
    color: var(--invite-ink);
    text-shadow: 1px 1px 2px var(--invite-shadow);
  }
  .services {
    position: absolute;
    left: 35px;
    top: 174px;
    font-family: "Fraunces", serif;
    font-weight: 700;
    font-size: 21px;
    color: var(--white);
    text-shadow: 1px 1px 2px rgba(0, 0, 0, 0.5);
    white-space: nowrap;
  }
  .paint-cans {
    position: absolute;
    left: 935px;
    top: 68px;
    width: 165px;
    height: 155px;
    border-radius: 40% 20% 0 40%;
    background: linear-gradient(160deg, var(--can-silver) 0%, var(--can-blue) 60%, var(--brand-blue) 100%);
  }
</style>
</head>
<body>
  <section class="banner">
    <div class="brand">
      <div class="brand-dot"></div>
      <div class="brand-name">Vardel<br>Paint</div>
    </div>
    <p class="headline">Don't settle for Dull, Lifeless Walls any longer</p>
    <p class="invite">Visit Vardel Paint today and<br>start painting your dream home!</p>
    <p class="services">Specializing in Indoor and Outdoor Painting, Epoxy Flooring, and More</p>
    <div class="paint-cans" role="img" aria-label="Two metal paint cans, one tipped over spilling bright blue paint onto the ground"></div>
  </section>
</body>
</html>
```